Coastal Bright Sweep Business Card

We are a cleaning and waste management company with the slogan "making waste to landfill a thing of the past". We would like a re-design of our current business card. On the front we want to continue to use our logo as the focus point. On the back, we want the whole thing re-done to be less busy. We want the staff member’s name, the job title, mobile number, email and website. We do not want the address on the card. We still want the green, black and blue colours used, but a new font for the information on the back. Please do not change the logo design at all. We are also thinking about using icons to replace the text ‘mobile, email, website’. The “events + commercial” banner needs to be incorporated somewhere and needs to read “events + commercial + waste”. Another important point for consideration is that we are very concerned about being environmentally sustainable and will be printing on recycled paper. All designs should be made to compliment this in regards to boldness and colouring. Please find attached our logo, our colour chart and an image of our current business card.

```html
<!DOCTYPE html>
<html lang="en">
<head>
<meta charset="utf-8">
<title>Coastal Bright Sweep – Business Card</title>
<link rel="stylesheet" href="https://fonts.googleapis.com/css2?family=Open+Sans:wght@400;700;800&display=swap">
<style>
  :root {
    --backdrop: #c8c5c6;
    --paper: #efefeb;
    --navy: #0f4a85;
    --lime: #b7d635;
    --sky: #3fc1e3;
    --ink: #17345c;
    --shadow: rgba(40, 36, 38, 0.28);
  }
  * { box-sizing: border-box; margin: 0; padding: 0; }
  html, body {
    width: 1200px; height: 1200px; overflow: hidden;
    background: var(--backdrop);
    font-family: "Open Sans", Arial, sans-serif;
  }
  .canvas { position: relative; width: 1200px; height: 1200px; }

  .card {
    position: absolute;
    width: 460px; height: 256px;
    background: var(--paper);
    box-shadow: 6px 18px 30px var(--shadow);
  }
  .card--front { left: 300px; top: 230px; }
  .card--back { left: 440px; top: 610px; }

  /* front */
  .front-name {
    position: absolute; inset: 0;
    display: flex; align-items: center; justify-content: center; gap: 12px;
  }
  .front-name__mark {
    width: 22px; height: 22px; border-radius: 50%; background: var(--lime);
  }
  .front-name__text {
    font-weight: 800; font-size: 27px; color: var(--navy); letter-spacing: 0.02em;
  }

  /* back */
  .services-band {
    position: absolute; left: 24px; top: 16px; width: 412px; height: 46px;
    background: var(--navy); border-radius: 6px;
    display: flex; align-items: center; padding-left: 18px;
    color: var(--lime); font-weight: 700; font-size: 14px; letter-spacing: 0.08em;
  }
  .contact {
    position: absolute; left: 62px; top: 84px; list-style: none;
  }
  .contact__row {
    position: relative; display: flex; align-items: center;
    color: var(--ink); font-size: 13px; letter-spacing: 0.09em;
  }
  .contact__icon { position: absolute; left: -30px; width: 18px; height: 18px; }
  .contact__row--name { font-size: 24px; font-weight: 700; color: var(--navy); letter-spacing: 0.08em; }
  .contact__role { color: var(--sky); font-size: 13px; letter-spacing: 0.1em; margin-top: 2px; }
  .contact__row--phone { margin-top: 8px; }
  .contact__row--email { margin-top: 24px; }
  .contact__row--web { margin-top: 18px; font-weight: 700; color: var(--navy); }

  .back-name {
    position: absolute; right: 22px; top: 92px; width: 96px;
    display: flex; align-items: center; gap: 6px;
  }
  .back-name__mark { flex: none; width: 10px; height: 10px; border-radius: 50%; background: var(--lime); }
  .back-name__text { font-weight: 800; font-size: 13px; line-height: 1.15; color: var(--navy); }
</style>
</head>
<body>
<main class="canvas">

  <section class="card card--front" aria-label="Business card front">
    <div class="front-name">
      <span class="front-name__mark"></span>
      <span class="front-name__text">Coastal Bright Sweep</span>
    </div>
  </section>

  <section class="card card--back" aria-label="Business card back">
    <div class="services-band">Events + Commercial + Waste Management</div>

    <ul class="contact">
      <li class="contact__row contact__row--name">
        <svg class="contact__icon" viewBox="0 0 18 18"><circle cx="9" cy="5.5" r="3.6" fill="#3fc1e3"/><path d="M2 17c0-4 3-6.5 7-6.5s7 2.5 7 6.5z" fill="#3fc1e3"/></svg>
        Jordan Ellery
      </li>
      <li class="contact__role">Client Manager</li>
      <li class="contact__row contact__row--phone">
        <svg class="contact__icon" viewBox="0 0 18 18"><rect x="4.5" y="1" width="9" height="16" rx="1.6" fill="none" stroke="#3fc1e3" stroke-width="1.5"/><circle cx="9" cy="14.2" r="0.9" fill="#3fc1e3"/></svg>
        0400 555 182
      </li>
      <li class="contact__row contact__row--email">
        <svg class="contact__icon" viewBox="0 0 18 18"><rect x="1.5" y="4" width="15" height="10" fill="none" stroke="#3fc1e3" stroke-width="1.5"/><path d="M1.5 4l7.5 6 7.5-6" fill="none" stroke="#3fc1e3" stroke-width="1.5"/></svg>
        jellery@coastalbrightsweep.com.au
      </li>
      <li class="contact__row contact__row--web">
        <svg class="contact__icon" viewBox="0 0 18 18"><g fill="none" stroke="#3fc1e3" stroke-width="1.3"><circle cx="9" cy="9" r="7"/><ellipse cx="9" cy="9" rx="3" ry="7"/><path d="M2 9h14M3.2 5h11.6M3.2 13h11.6"/></g></svg>
        www.coastalbrightsweep.com.au
      </li>
    </ul>

    <div class="back-name">
      <span class="back-name__mark"></span>
      <span class="back-name__text">Coastal Bright Sweep</span>
    </div>
  </section>

</main>
</body>
</html>
```